VFX Company Business Card Design Project

The Ember Vale is a decentralized Visual Effects Studio servicing the television and feature film industries.
Project Brief:
Take our logo that was previously designed on Pixel Harbor and make a double sided business card.
Requirements:
- Card MUST be double sided.
- Front of card MUST have the yellow part of our logo against the dark grey background.
- Back of card is completely up to the designer.
- Back of card must include the complete company logo.
Please follow these File Preparation guidelines:
http://printmoor.example/infopage?file=filetype_en&s=PrintMoor_new&lang=en
Industry/Entity Type
Business
Look and feel
Each slider illustrates characteristics of the customer's brand and the style your logo design should communicate.

```html
<!DOCTYPE html>
<html lang="en">
<head>
<meta charset="utf-8">
<title>The Ember Vale – Business Card</title>
<link rel="stylesheet" href="https://fonts.googleapis.com/css2?family=Arimo:wght@400;700&display=swap">
<style>
  :root {
    --backdrop: #1c1c1c;
    --card-dark: #2b2b2b;
    --card-slate: #6c777a;
    --ember-yellow: #f5be1e;
    --paper-white: #f2f2ee;
    --soft-grey: #b9bfc1;
  }
  * { box-sizing: border-box; margin: 0; padding: 0; }
  html, body {
    width: 1200px; height: 900px; overflow: hidden;
    background: var(--backdrop);
    font-family: "Arimo", Arial, sans-serif;
  }
  .stage {
    width: 1200px; height: 900px;
    display: flex; flex-direction: column; align-items: center; justify-content: center;
    gap: 40px;
  }
  .card {
    width: 640px; height: 366px;
    position: relative; overflow: hidden;
    box-shadow: 0 8px 24px rgba(0,0,0,.55);
  }

  /* Details side */
  .card-details { background: var(--card-slate); }
  .card-details .brand-band {
    position: absolute; left: 0; top: 0; width: 100%; height: 150px;
    background: var(--card-dark);
    display: flex; align-items: center; padding-left: 44px; gap: 16px;
  }
  .slate-field { position: absolute; left: 0; top: 150px; width: 100%; height: 216px; background: var(--card-slate); }
  .brand-mark { display: flex; align-items: center; gap: 14px; }
  .brand-dot { width: 34px; height: 34px; border-radius: 50%; background: var(--ember-yellow); }
  .brand-name {
    font-weight: 700; color: var(--ember-yellow); font-size: 40px; letter-spacing: 1px;
  }
  .brand-tagline {
    color: var(--soft-grey); font-size: 13px; letter-spacing: 6px; text-transform: uppercase;
    margin-top: 4px;
  }
  .holder { position: absolute; left: 44px; top: 222px; }
  .holder-name { color: var(--ember-yellow); font-weight: 700; font-size: 26px; }
  .holder-role { color: var(--paper-white); font-size: 15px; margin-top: 6px; }
  .holder-web { color: var(--paper-white); font-size: 19px; margin-top: 22px; }
  .holder-web span { color: var(--ember-yellow); }
  .contact-list {
    position: absolute; right: 40px; top: 176px; list-style: none;
    font-size: 14px; line-height: 25px; color: var(--paper-white);
  }
  .contact-list .label { color: var(--ember-yellow); display: inline-block; width: 62px; text-align: right; margin-right: 6px; }

  /* Logo side */
  .card-logo { background: var(--card-dark); }
  .card-logo .texture { position: absolute; inset: 0; background: linear-gradient(135deg, #2e2e2e, #262626); }
  .logo-lockup {
    position: absolute; inset: 0;
    display: flex; flex-direction: column; align-items: center; justify-content: center;
  }
  .logo-lockup .brand-name { font-size: 52px; }
  .logo-lockup .brand-dot { width: 42px; height: 42px; }
  .logo-lockup .brand-tagline { font-size: 16px; letter-spacing: 9px; margin-top: 8px; }
  .logo-web {
    color: var(--ember-yellow); font-size: 17px; letter-spacing: 5px; margin-top: 30px;
  }
</style>
</head>
<body>
<main class="stage">
  <section class="card card-details">
    <div class="brand-band">
      <div>
        <div class="brand-mark">
          <span class="brand-dot"></span>
          <span class="brand-name">The Ember Vale</span>
        </div>
        <div class="brand-tagline">Virtual Studio</div>
      </div>
    </div>
    <div class="slate-field" role="img" aria-label="Faint repeated studio name pattern on slate grey"></div>
    <div class="holder">
      <div class="holder-name">Marcus Lindqvist</div>
      <div class="holder-role">Partner/Sales Manager</div>
      <div class="holder-web">www.<span>embervale</span>.example</div>
    </div>
    <ul class="contact-list">
      <li><span class="label">phone:</span>+1 555 014 2230</li>
      <li><span class="label">mobile:</span>+1 555 014 2230</li>
      <li><span class="label">fax:</span>+1 555 014 2230</li>
      <li><span class="label">email:</span>studio@embervale.example</li>
    </ul>
  </section>

  <section class="card card-logo">
    <div class="texture" role="img" aria-label="Faint repeated studio name pattern on dark grey"></div>
    <div class="logo-lockup">
      <div class="brand-mark">
        <span class="brand-dot"></span>
        <span class="brand-name">The Ember Vale</span>
      </div>
      <div class="brand-tagline">Virtual Studio</div>
      <div class="logo-web">WWW.EMBERVALE.EXAMPLE</div>
    </div>
  </section>
</main>
</body>
</html>
```